AUSTRALIA SUPPLEMENT - Protein label design - CREATIVE, FEMININE, UNIQUE

I need help with the design of what will be my line of supplements. (Protein, plant base, collagen , BCAAs, etc)
I'm starting off with protein isolate - with the flavours VANILLA, CHOCOLATE, BOYSENBERRY, HONEYCOMB.
I need help with the design of what the product will look like for my range.
(Great opportunity for further work)

Looking for a unique, elegant, stand out, feminine design, some slight sparkle or something that stands out on a shelf.
With symbols to represent what's in it, raised text. with some quirky cute things on it. (not sure what) Something that captured young womens eyes and easy to understand. things on it that appeals to women such as
LOW CALORIE, GREAT TASTING, GLUTEN FREE, 100 NATURAL, NATURALLY SWEETENED, HIGH PROTEIN.etc and whatever you can think of (open to ideas) but within KMO guidelines.

Mostly just after the look and creativity of what the front will look like. Don't have to worry about the back area.

My market will be for females aged 18-35

I have a activewear line called DORUMEN which will go with this. which I will attach the logo below amongst some other things that match my packaging. (again open to ideas)

I have attached a label of what one will look like( EXAMPLE).
. Among others that look nice But again I want to be different, unique to stand out. I don't want it to look like these. it's just the only ones I found online I liked that suit my market.

Feel free to ask any questions! :)
Updates

Extending time as I want this to be to be what will be on the shelves of many stores. I know that needs time to be able to do a quality job.

Target Market(s)

18-35

Industry/Entity Type

Supplement

Font styles to use
Serif
Script

Colors
f9d9e8
ffffff
fbd3d4
ecf7fb
e4daeb
cfeae6
eea4c8
fdfad7
f59195

Requirements
Must have
• Word - DORUMEN
PROTEIN ISOLATE
FLAVOUR
SYMBOLS

Looking for a unique, elegant, stand out, colour, feminine design, some slight sparkle or something that stands out on a shelf.

IT WILL BE ON A WHITE TUB or CLEAR - Perhaps detail on the lid
Nice to have
• Looking for a unique, elegant, stand out, colour, feminine design, some slight sparkle or something that stands out on a shelf. Something artsy.

will be on a white or clear tub with a white label background (possibly)
Should not have
• I don’t want it dark looking.
Something bright, vibrant, whites, pinks, sparkles (maybe) colours.

I don't want the word activewear on it.

```html
<!DOCTYPE html>
<html lang="en">
<head>
<meta charset="utf-8">
<title>Dorumen Protein Isolate – Flavour Range</title>
<link href="https://fonts.googleapis.com/css2?family=Lato:wght@400;700&display=swap" rel="stylesheet">
<style>
  :root {
    --stage: #383838;
    --white: #ffffff;
    --ink: #111111;
    --flavour-box: #000000;

    --vanilla-paper: #fbfae8;
    --vanilla-wash: #e6df93;
    --vanilla-band-a: #d8d28c;
    --vanilla-band-b: #908c6a;
    --vanilla-seal: #6b685b;
    --vanilla-name: #ffffff;

    --choc-paper: #f4f0ea;
    --choc-wash: #cdbfae;
    --choc-band-a: #cdb697;
    --choc-band-b: #4d3817;
    --choc-seal: #4f3a15;
    --choc-name: #dcc6a6;

    --berry-paper: #f6ecf1;
    --berry-wash: #c79db4;
    --berry-band-a: #c795b0;
    --berry-band-b: #86295b;
    --berry-seal: #8a2760;
    --berry-name: #e25fa9;

    --honey-paper: #fffbe6;
    --honey-wash: #f7c85a;
    --honey-band-a: #f8de3a;
    --honey-band-b: #d08200;
    --honey-seal: #d08b12;
    --honey-name: #f6ea3c;
  }

  * { margin: 0; padding: 0; box-sizing: border-box; }

  html, body {
    width: 1200px;
    height: 1200px;
    overflow: hidden;
    background: var(--stage);
    font-family: "Lato", sans-serif;
  }

  .range {
    position: relative;
    width: 1200px;
    height: 1200px;
  }

  .label {
    position: absolute;
    width: 494px;
    height: 492px;
    background: var(--white);
    box-shadow: 0 4px 14px rgba(0,0,0,0.35);
    overflow: hidden;
  }
  .label--vanilla     { left: 82px;  top: 86px;  }
  .label--chocolate   { left: 617px; top: 86px;  }
  .label--boysenberry { left: 82px;  top: 622px; }
  .label--honeycomb   { left: 617px; top: 622px; }

  .label__artwork {
    position: absolute;
    left: 0; top: 0;
    width: 494px;
    height: 357px;
  }
  .label--vanilla .label__artwork {
    background:
      radial-gradient(ellipse 120px 140px at 40px 220px, var(--vanilla-wash), transparent 75%),
      radial-gradient(ellipse 140px 110px at 470px 60px, var(--vanilla-wash), transparent 75%),
      radial-gradient(ellipse 160px 80px at 420px 320px, var(--vanilla-wash), transparent 75%),
      var(--vanilla-paper);
  }
  .label--chocolate .label__artwork {
    background:
      radial-gradient(ellipse 120px 140px at 40px 220px, var(--choc-wash), transparent 75%),
      radial-gradient(ellipse 140px 110px at 470px 60px, var(--choc-wash), transparent 75%),
      radial-gradient(ellipse 160px 80px at 420px 320px, var(--choc-wash), transparent 75%),
      var(--choc-paper);
  }
  .label--boysenberry .label__artwork {
    background:
      radial-gradient(ellipse 120px 140px at 40px 220px, var(--berry-wash), transparent 75%),
      radial-gradient(ellipse 140px 110px at 470px 60px, var(--berry-wash), transparent 75%),
      radial-gradient(ellipse 160px 80px at 420px 320px, var(--berry-wash), transparent 75%),
      var(--berry-paper);
  }
  .label--honeycomb .label__artwork {
    background:
      radial-gradient(ellipse 120px 140px at 40px 220px, var(--honey-wash), transparent 75%),
      radial-gradient(ellipse 140px 110px at 470px 60px, var(--honey-wash), transparent 75%),
      radial-gradient(ellipse 160px 80px at 420px 320px, var(--honey-wash), transparent 75%),
      var(--honey-paper);
  }

  .label__flavour {
    position: absolute;
    left: 137px; top: 0;
    width: 218px; height: 102px;
    background: var(--flavour-box);
    display: flex;
    align-items: flex-end;
    justify-content: center;
    padding-bottom: 12px;
    font-size: 23px;
    letter-spacing: 0.14em;
  }
  .label--vanilla .label__flavour     { color: var(--vanilla-name); letter-spacing: 0.3em; }
  .label--chocolate .label__flavour   { color: var(--choc-name); }
  .label--boysenberry .label__flavour { color: var(--berry-name); letter-spacing: 0.06em; }
  .label--honeycomb .label__flavour   { color: var(--honey-name); letter-spacing: 0.08em; }

  .label__seal {
    position: absolute;
    left: 341px; top: 80px;
    width: 104px; height: 104px;
    border-radius: 50%;
  }
  .label--vanilla .label__seal     { background: var(--vanilla-seal); }
  .label--chocolate .label__seal   { background: var(--choc-seal); }
  .label--boysenberry .label__seal { background: var(--berry-seal); }
  .label--honeycomb .label__seal   { background: var(--honey-seal); }

  .brand {
    position: absolute;
    left: 74px; top: 210px;
    display: flex;
    align-items: center;
    gap: 12px;
  }
  .brand__dot {
    width: 40px; height: 40px;
    border-radius: 50%;
    border: 2px solid var(--ink);
  }
  .brand__name {
    font-size: 44px;
    font-weight: 400;
    color: var(--ink);
    letter-spacing: 0.08em;
  }

  .label__claim {
    position: absolute;
    left: 228px; top: 234px;
    font-size: 17px;
    letter-spacing: 0.09em;
    color: var(--ink);
    transform: translateY(30px);
  }

  .label__band {
    position: absolute;
    left: 0; top: 357px;
    width: 494px; height: 67px;
    display: flex;
    align-items: center;
    justify-content: center;
    color: var(--white);
    font-size: 39px;
    letter-spacing: 0.02em;
  }
  .label--vanilla .label__band     { background: linear-gradient(90deg, var(--vanilla-band-a), var(--vanilla-band-b)); }
  .label--chocolate .label__band   { background: linear-gradient(90deg, var(--choc-band-a), var(--choc-band-b) 70%); }
  .label--boysenberry .label__band { background: linear-gradient(90deg, var(--berry-band-a), var(--berry-band-b) 60%); }
  .label--honeycomb .label__band   { background: linear-gradient(90deg, var(--honey-band-a), var(--honey-band-b)); }

  .label__benefits {
    position: absolute;
    left: 0; top: 424px;
    width: 494px; height: 68px;
    display: flex;
    align-items: center;
    justify-content: center;
    font-size: 12px;
    letter-spacing: 0.12em;
    color: var(--ink);
    word-spacing: 0.1em;
  }
  .label__benefits span + span::before {
    content: "I";
    margin: 0 10px;
    font-size: 10px;
  }
</style>
</head>
<body>
<main class="range">

  <section class="label label--vanilla">
    <div class="label__artwork" role="img" aria-label="Soft vanilla watercolour washes with fine leaf sprigs"></div>
    <div class="label__flavour">VANILLA</div>
    <div class="label__seal" aria-label="Natural seal"></div>
    <div class="brand"><span class="brand__dot"></span><span class="brand__name">DORUMEN</span></div>
    <div class="label__claim">HIGH PROTEIN</div>
    <div class="label__band">PROTEIN ISOLATE</div>
    <div class="label__benefits"><span>LOW CALORIE</span><span>GLUTEN FREE</span><span>NATURALLY SWEETENED</span></div>
  </section>

  <section class="label label--chocolate">
    <div class="label__artwork" role="img" aria-label="Soft cocoa watercolour washes with fine leaf sprigs"></div>
    <div class="label__flavour">CHOCOLATE</div>
    <div class="label__seal" aria-label="Natural seal"></div>
    <div class="brand"><span class="brand__dot"></span><span class="brand__name">DORUMEN</span></div>
    <div class="label__claim">HIGH PROTEIN</div>
    <div class="label__band">PROTEIN ISOLATE</div>
    <div class="label__benefits"><span>LOW CALORIE</span><span>GLUTEN FREE</span><span>NATURALLY SWEETENED</span></div>
  </section>

  <section class="label label--boysenberry">
    <div class="label__artwork" role="img" aria-label="Soft berry watercolour washes with fine leaf sprigs"></div>
    <div class="label__flavour">BOYSENBERRY</div>
    <div class="label__seal" aria-label="Natural seal"></div>
    <div class="brand"><span class="brand__dot"></span><span class="brand__name">DORUMEN</span></div>
    <div class="label__claim">HIGH PROTEIN</div>
    <div class="label__band">PROTEIN ISOLATE</div>
    <div class="label__benefits"><span>LOW CALORIE</span><span>GLUTEN FREE</span><span>NATURALLY SWEETENED</span></div>
  </section>

  <section class="label label--honeycomb">
    <div class="label__artwork" role="img" aria-label="Soft honey watercolour washes with fine leaf sprigs"></div>
    <div class="label__flavour">HONEYCOMB</div>
    <div class="label__seal" aria-label="Natural seal"></div>
    <div class="brand"><span class="brand__dot"></span><span class="brand__name">DORUMEN</span></div>
    <div class="label__claim">HIGH PROTEIN</div>
    <div class="label__band">PROTEIN ISOLATE</div>
    <div class="label__benefits"><span>LOW CALORIE</span><span>GLUTEN FREE</span><span>NATURALLY SWEETENED</span></div>
  </section>

</main>
</body>
</html>
```